KORBALT

The business want a professional looking business card. We have a scetch we will add but want the extra upgrade, and would like more suggestions for variations of our business cards.

```html
<!DOCTYPE html>
<html lang="en">
<head>
<meta charset="utf-8">
<title>KORBALT – Business Card</title>
<link rel="stylesheet" href="https://fonts.googleapis.com/css2?family=Cinzel:wght@600&family=Hind:wght@400;600&family=Marcellus&display=swap">
<style>
  :root {
    --backdrop: #606060;
    --paper: #ffffff;
    --ink: #111111;
    --black: #000000;
    --gold: #9a7430;
    --gold-light: #e9d07a;
    --gold-mid: #c9a04a;
    --gold-deep: #7a5530;
    --gold-pale: #f3df8c;
  }
  * { box-sizing: border-box; margin: 0; padding: 0; }
  html, body {
    width: 1200px; height: 1200px; overflow: hidden;
    background: var(--backdrop);
  }
  .card {
    position: absolute; left: 208px; width: 784px; height: 469px;
    overflow: hidden; box-shadow: 3px 5px 6px rgba(0,0,0,.35);
  }
  .card--front { top: 115px; background: var(--paper); }
  .card--back  { top: 617px; }

  .front-art { position: absolute; inset: 0; }

  .company {
    position: absolute; left: 63px; top: 62px; height: 57px;
    border-left: 1.5px solid var(--gold); padding-left: 14px;
    font-family: "Cinzel", serif; font-weight: 600; font-size: 31px;
    line-height: 32px; color: var(--gold); margin-top: -6px;
  }
  .person { position: absolute; left: 63px; top: 193px; }
  .person__name {
    font-family: "Hind", sans-serif; font-weight: 600; font-size: 27px;
    color: var(--gold); letter-spacing: .3px; line-height: 34px;
  }
  .person__role {
    font-family: "Hind", sans-serif; font-weight: 400; font-size: 24px;
    color: var(--ink); line-height: 30px;
  }
  .person__rule {
    width: 64px; height: 1.5px; background: var(--gold); margin-top: 10px;
  }
  .contacts { position: absolute; left: 63px; top: 308px; list-style: none; }
  .contacts li {
    display: flex; align-items: center; height: 37.5px;
    font-family: "Hind", sans-serif; font-size: 21px; color: var(--ink);
  }
  .contacts svg { width: 18px; height: 18px; margin-right: 14px; flex: none; }

  .badge-name {
    font-family: "Marcellus", serif; fill: var(--gold-light);
  }
  .badge-tag {
    font-family: "Hind", sans-serif; fill: var(--gold-light);
  }

  .back-surface {
    position: absolute; inset: 0;
    background: linear-gradient(135deg, var(--gold-light) 0%, var(--gold-mid) 30%, var(--gold-deep) 60%, #a88148 80%, var(--gold-pale) 100%);
  }
  .back-logo {
    position: absolute; left: 0; right: 0; top: 296px; text-align: center;
    color: var(--black);
  }
  .back-logo__name {
    font-family: "Marcellus", serif; font-size: 58px; letter-spacing: 18px;
    line-height: 64px; padding-left: 18px;
  }
  .back-logo__tag {
    font-family: "Hind", sans-serif; font-size: 20px; letter-spacing: 9px;
    line-height: 26px; margin-top: 4px; padding-left: 9px;
  }
</style>
</head>
<body>

<section class="card card--front">
  <svg class="front-art" viewBox="0 0 784 469" width="784" height="469">
    <defs>
      <linearGradient id="goldField" x1="0" y1="0" x2="1" y2="1">
        <stop offset="0" stop-color="#c39a48"/>
        <stop offset=".45" stop-color="#8a6232"/>
        <stop offset=".75" stop-color="#b8944d"/>
        <stop offset="1" stop-color="#efd880"/>
      </linearGradient>
      <linearGradient id="badgeRim" x1="0" y1="0" x2="1" y2="1">
        <stop offset="0" stop-color="#f3df8c"/>
        <stop offset=".5" stop-color="#a67c36"/>
        <stop offset="1" stop-color="#e9cf7a"/>
      </linearGradient>
      <filter id="badgeShadow" x="-30%" y="-30%" width="160%" height="160%">
        <feDropShadow dx="-6" dy="10" stdDeviation="10" flood-color="#000" flood-opacity=".35"/>
      </filter>
    </defs>
    <polygon class="band-black" fill="var(--black)" points="404,0 784,0 784,469 385,469 484,314 472,160"/>
    <polygon class="gold-field" role="img" aria-label="Gold faceted geometric pattern" fill="url(#goldField)" points="423,0 784,0 784,469 407,469 500,314 490,160"/>
    <polygon class="corner-stripe" fill="var(--paper)" points="648,0 661,0 784,120 784,133"/>
    <polygon class="corner-black" fill="var(--black)" points="661,0 784,0 784,120"/>
    <g class="badge" transform="translate(570 234) rotate(45)" filter="url(#badgeShadow)">
      <rect x="-116" y="-116" width="232" height="232" rx="16" fill="var(--black)" stroke="url(#badgeRim)" stroke-width="6"/>
    </g>
    <text class="badge-name" x="573" y="266" text-anchor="middle" font-size="29" letter-spacing="7">KORBALT</text>
    <text class="badge-tag" x="573" y="292" text-anchor="middle" font-size="12" letter-spacing="4">SINCE 2026</text>
  </svg>

  <h1 class="company">KORBALT<br>HALVORSEN</h1>

  <div class="person">
    <p class="person__name">ERIK ANDERS HALVORSEN</p>
    <p class="person__role">CEO &amp; Founder</p>
    <div class="person__rule"></div>
  </div>

  <ul class="contacts">
    <li>
      <svg viewBox="0 0 18 18" aria-hidden="true"><rect x="4.5" y="1" width="9" height="16" rx="1.5" fill="none" stroke="var(--gold)" stroke-width="1.6"/><circle cx="9" cy="14.3" r="1" fill="var(--gold)"/></svg>
      00 471 555 0192
    </li>
    <li>
      <svg viewBox="0 0 18 18" aria-hidden="true"><rect x="1" y="4" width="16" height="10" fill="var(--gold)"/><polyline points="1,4 9,10 17,4" fill="none" stroke="#fff" stroke-width="1.2"/><polyline points="1,14 7,9 M11,9 17,14" fill="none" stroke="#fff" stroke-width="1"/></svg>
      korbalt.llc@postmail.com
    </li>
    <li>
      <svg viewBox="0 0 18 18" aria-hidden="true"><g fill="none" stroke="var(--gold)" stroke-width="1.3"><circle cx="9" cy="9" r="7.5"/><ellipse cx="9" cy="9" rx="3.3" ry="7.5"/><line x1="1.5" y1="9" x2="16.5" y2="9"/><line x1="3" y1="5" x2="15" y2="5"/><line x1="3" y1="13" x2="15" y2="13"/></g></svg>
      www.korbalt.llc
    </li>
  </ul>
</section>

<section class="card card--back">
  <div class="back-surface" role="img" aria-label="Gold faceted geometric pattern"></div>
  <div class="back-logo">
    <p class="back-logo__name">KORBALT</p>
    <p class="back-logo__tag">SINCE 2026</p>
  </div>
</section>

</body>
</html>
```